Crestline Gas and Plumbing Business Card Design

I am after a business card design for my plumbing business called 'Crestline Gas & Plumbing'. I do all types of plumbing and gas work and specialise in general maintenance plumbing. Would like to see designs using current logo

Industry/Entity Type

Plumbing

Contact Information for Business Card

Name - Dale Whitcombe
Phone number - 0455163027
Email - admin@crestlinegasandplumbing.example.com.au
ABN - 68204915336

```html
<!DOCTYPE html>
<html lang="en">
<head>
<meta charset="utf-8">
<title>Crestline Gas &amp; Plumbing – Business Card</title>
<link rel="stylesheet" href="https://fonts.googleapis.com/css2?family=Exo+2:wght@800&family=Open+Sans:wght@400;700&display=swap">
<style>
  :root {
    --page: #d9d9dc;
    --card-black: #17171a;
    --brand-blue: #2a74d8;
    --orange-start: #ff9a1f;
    --orange-end: #f26a2a;
    --blue-start: #2f3fae;
    --blue-mid: #1c7fd0;
    --blue-end: #2b3aa6;
    --white: #ffffff;
    --muted: #3a3a40;
  }
  * { box-sizing: border-box; margin: 0; padding: 0; }
  html, body { width: 1200px; height: 960px; overflow: hidden; }
  body {
    background: var(--page);
    display: flex;
    flex-direction: column;
    align-items: center;
    justify-content: center;
    gap: 40px;
    font-family: "Open Sans", Arial, sans-serif;
  }
  .card {
    position: relative;
    width: 700px;
    height: 400px;
    background: var(--card-black);
    border-radius: 6px;
    overflow: hidden;
    box-shadow: 0 10px 30px rgba(0,0,0,0.25);
  }

  /* Back side */
  .card-back {
    display: flex;
    align-items: center;
    justify-content: center;
    gap: 18px;
  }
  .brand-mark {
    width: 44px;
    height: 44px;
    border-radius: 50%;
    background: var(--muted);
  }
  .brand-name {
    font-family: "Exo 2", Arial, sans-serif;
    font-weight: 800;
    text-transform: uppercase;
    letter-spacing: 1px;
  }
  .card-back .brand-name {
    color: var(--muted);
    font-size: 34px;
  }

  /* Front side */
  .card-front .bands {
    position: absolute;
    inset: 0;
  }
  .card-front .brand-name {
    position: absolute;
    left: 40px;
    top: 44px;
    color: var(--brand-blue);
    font-size: 30px;
    line-height: 1.1;
  }
  .holder-name {
    position: absolute;
    left: 40px;
    top: 152px;
    color: var(--white);
    font-weight: 700;
    font-size: 26px;
    letter-spacing: 1px;
    text-transform: uppercase;
  }
  .contact-list {
    position: absolute;
    left: 40px;
    top: 224px;
    list-style: none;
    color: var(--white);
    font-size: 16px;
    line-height: 28px;
  }
  .contact-list li {
    display: flex;
    align-items: center;
    gap: 10px;
  }
  .contact-list svg { width: 15px; height: 15px; fill: var(--white); }
</style>
</head>
<body>

  <section class="card card-back" aria-label="Card back">
    <span class="brand-mark" aria-hidden="true"></span>
    <span class="brand-name">Crestline Gas &amp; Plumbing</span>
  </section>

  <section class="card card-front" aria-label="Card front">
    <svg class="bands" viewBox="0 0 700 400" aria-hidden="true">
      <defs>
        <linearGradient id="orangeBand" x1="0" y1="0" x2="1" y2="0">
          <stop offset="0" stop-color="var(--orange-start)"/>
          <stop offset="1" stop-color="var(--orange-end)"/>
        </linearGradient>
        <linearGradient id="blueBand" x1="0" y1="0" x2="1" y2="1">
          <stop offset="0" stop-color="var(--blue-start)"/>
          <stop offset="0.5" stop-color="var(--blue-mid)"/>
          <stop offset="1" stop-color="var(--blue-end)"/>
        </linearGradient>
      </defs>
      <path d="M0 140 H390 Q418 140 430 166 L452 214 H0 Z" fill="url(#orangeBand)"/>
      <path d="M0 204 H440 Q462 204 472 224 L490 258 H700 V400 H0 Z" fill="url(#blueBand)"/>
    </svg>

    <h1 class="brand-name">Crestline<br>Gas &amp; Plumbing</h1>

    <p class="holder-name">Dale Whitcombe</p>

    <ul class="contact-list">
      <li>
        <svg viewBox="0 0 24 24" aria-hidden="true"><path d="M6.6 10.8a15.1 15.1 0 0 0 6.6 6.6l2.2-2.2c.3-.3.7-.4 1-.2 1.1.4 2.3.6 3.6.6.6 0 1 .4 1 1V20c0 .6-.4 1-1 1A17 17 0 0 1 3 4c0-.6.4-1 1-1h3.5c.6 0 1 .4 1 1 0 1.3.2 2.5.6 3.6.1.3 0 .7-.2 1z"/></svg>
        <span>0455163027</span>
      </li>
      <li>
        <svg viewBox="0 0 24 24" aria-hidden="true"><path d="M2 5h20v14H2z M4 7v.4l8 5.2 8-5.2V7z" fill-rule="evenodd"/></svg>
        <span>admin@crestlinegasandplumbing.example.com.au</span>
      </li>
      <li><span>ABN 68204915336</span></li>
    </ul>
  </section>

</body>
</html>
```